Need a business card design. I am a Self Empowerment Life Coach.

A Life Coach is - a professional relationship designed to enhance an individual's ability to focus, make effective changes, develop oneself, achieve desired goals and maximize success in life. Coaching is about getting the very best out of someone and enabling them to make decisions that will improve their life. It is a unique way to help people look at where they are now and where they would like to be, and helps bridge the gap.

Bright Path Coaching is motivational, inspiring, positive, exciting and action driven. By raising awareness and encouraging others to take responsibility for their life, coaching can help people rise to their challenge and go further than you ever thought possible.

Industry/Entity Type

Business

Other font styles liked:
• Bookman Old Style

Requirements
Must have
• Marla Thorncastle, QTV-AR
• Self Empowerment Coach
• 318.557.6021
• mt@thebloomingpathcoach.example
• The attached logo
Nice to have
• I would like to see some designs portrait and some landscape

```html
<!DOCTYPE html>
<html lang="en">
<head>
<meta charset="utf-8">
<title>Bright Path Coaching – Business Card</title>
<link rel="stylesheet" href="https://fonts.googleapis.com/css2?family=Josefin+Sans:wght@300;700&family=Libre+Baskerville&display=swap">
<style>
  :root {
    --page-bg: #f1f1f3;
    --card-bg: #ffffff;
    --ink: #1c1c1c;
    --ink-soft: #3a3a3a;
    --accent-grey: #9a9a9a;
    --rule: #2a2a2a;
  }
  * { box-sizing: border-box; margin: 0; padding: 0; }
  html, body {
    width: 1000px;
    height: 1200px;
    overflow: hidden;
    background: var(--page-bg);
  }
  .card {
    position: absolute;
    left: 280px;
    top: 215px;
    width: 440px;
    height: 770px;
    background: var(--card-bg);
    box-shadow: 0 8px 30px rgba(0,0,0,0.08);
  }
  .brand {
    position: absolute;
    left: 70px;
    top: 150px;
    display: flex;
    align-items: center;
    gap: 16px;
  }
  .brand-dot {
    width: 44px;
    height: 44px;
    border-radius: 50%;
    background: var(--accent-grey);
    flex: none;
  }
  .brand-name {
    font-family: "Josefin Sans", sans-serif;
    font-weight: 700;
    font-size: 40px;
    line-height: 1.0;
    color: var(--ink);
    text-transform: uppercase;
    letter-spacing: 1px;
  }
  .divider {
    position: absolute;
    left: 60px;
    top: 318px;
    width: 320px;
    height: 2px;
    background: var(--rule);
  }
  .tagline {
    position: absolute;
    left: 60px;
    top: 332px;
    font-family: "Josefin Sans", sans-serif;
    font-weight: 300;
    color: var(--ink);
  }
  .tagline-lead {
    font-size: 17px;
    letter-spacing: 1px;
    text-transform: uppercase;
  }
  .tagline-punch {
    margin-top: 4px;
    font-size: 54px;
    letter-spacing: 10px;
    line-height: 1;
  }
  .contact {
    position: absolute;
    left: 0;
    right: 0;
    top: 500px;
    text-align: center;
    font-family: "Libre Baskerville", serif;
    font-size: 16px;
    line-height: 1.55;
    color: var(--ink-soft);
  }
</style>
</head>
<body>
  <main class="card">
    <div class="brand">
      <span class="brand-dot"></span>
      <span class="brand-name">Bright Path<br>Coaching</span>
    </div>
    <div class="divider"></div>
    <div class="tagline">
      <p class="tagline-lead">Shift from ho hum to</p>
      <p class="tagline-punch">TA DA!</p>
    </div>
    <address class="contact" style="font-style: normal;">
      <p>Marla Thorncastle, QTV-AR</p>
      <p>Self Empowerment Coach</p>
      <p>318.557.6021</p>
      <p>mt@thebloomingpathcoach.example</p>
    </address>
  </main>
</body>
</html>
```